EmberGuard Larkton- Making Larkton A Wildfire Adapted Community

Design a two complimentary graphics with text that can be used for a banner and "mini-billboard" to promote the project and encourage citizens to go to the webpage to learn more. Using the attached document as examples of what we want the two banners to say.
The goal of EmberGuard Larkton is to plan and prepare so if an urban wildfire occurs, catastrophic loss can be avoided. EmberGuard Larkton focuses on reducing the risk of and catastrophic losses to resources and private property on private land in Larkton, MT. Property owners are encouraged to be proactive to address hazardous fuel conditions on their property, reduce structure ignition potential within their home ignition zone and employ wildfire resilient principles to sustain a fire adapted home, property and community. Ember showers from a wildfire next to the city is the biggest concern.

Target Market(s)

Residents in the project area of Larkton. Signs and banners will be displayed on public lands and private yeards

Font styles to use
Sans Serif

Requirements
Must have
• Graphics, use of the ValleyRidge Ember Watch Council logo. Must incorporate the text that is part of the attachment.
Nice to have
• Get people's attention. A simple graphic that get's people's attention.
Should not have
• small details.

```html
<!DOCTYPE html>
<html lang="en">
<head>
<meta charset="utf-8">
<title>EmberGuard Larkton – Mini-Billboard and Banner</title>
<link href="https://fonts.googleapis.com/css2?family=Bebas+Neue&family=Oswald:wght@300;400;500&display=swap" rel="stylesheet">
<style>
  :root {
    --board-bg: #3a3a3a;
    --card-bg: #f1f1f1;
    --card-sheen: #fbfbfb;
    --alert-red: #a8071a;
    --forest-green: #17473b;
    --ink: #1c1c1c;
    --white: #ffffff;
    --scene-sky: #f3f3f3;
    --scene-leaf: #4e9e3a;
    --scene-flame: #f06a1c;
  }
  * { margin: 0; padding: 0; box-sizing: border-box; }
  html, body { width: 1064px; height: 1200px; overflow: hidden; }
  body {
    position: relative;
    background: var(--board-bg);
    font-family: "Oswald", sans-serif;
    color: var(--ink);
  }
  .section-label {
    position: absolute;
    left: 0; width: 1064px;
    text-align: center;
    font-family: "Bebas Neue", sans-serif;
    font-size: 44px;
    color: var(--white);
    line-height: 1;
  }
  .section-label--billboard { top: 66px; }
  .section-label--banner { top: 1102px; }

  .sign {
    position: absolute;
    overflow: hidden;
    background: linear-gradient(125deg, var(--card-bg) 0%, var(--card-sheen) 35%, var(--card-bg) 55%, var(--card-sheen) 80%, var(--card-bg) 100%);
    box-shadow: 0 2px 6px rgba(0,0,0,.4);
  }
  .sign--billboard { left: 120px; top: 144px; width: 820px; height: 273px; }
  .sign--banner { left: 122px; top: 460px; width: 818px; height: 613px; }

  .headline {
    position: absolute;
    font-family: "Bebas Neue", sans-serif;
    color: var(--alert-red);
    white-space: nowrap;
  }
  .sign--billboard .headline { left: 28px; top: 24px; font-size: 44px; line-height: 40px; }
  .sign--banner .headline { left: 35px; top: 45px; font-size: 58px; line-height: 60px; }

  .lede {
    position: absolute; left: 28px; top: 121px;
    font-size: 15px; font-weight: 300; line-height: 20px;
  }

  .call-out {
    position: absolute;
    font-family: "Bebas Neue", sans-serif;
    color: var(--forest-green);
    font-size: 76px; line-height: 1; letter-spacing: 1px;
    left: 38px; top: 258px;
  }
  .stakes {
    position: absolute; left: 39px; top: 345px;
    font-family: "Oswald", sans-serif; font-weight: 400;
    font-size: 36px; line-height: 37px; text-transform: uppercase;
    transform: scaleX(.88); transform-origin: left top;
  }

  .web-band {
    position: absolute; left: 0;
    background: var(--forest-green);
    color: var(--white);
  }
  .sign--billboard .web-band { top: 178px; width: 353px; height: 79px; clip-path: polygon(0 0, 317px 0, 100% 100%, 0 100%); padding: 10px 0 0 28px; }
  .sign--banner .web-band { top: 500px; width: 386px; height: 85px; clip-path: polygon(0 0, 348px 0, 100% 100%, 0 100%); padding: 10px 0 0 33px; }
  .web-band__lead { font-family: "Bebas Neue", sans-serif; font-size: 21px; line-height: 1; }
  .web-band__url { font-family: "Bebas Neue", sans-serif; font-size: 42px; line-height: 1; margin-top: 4px; letter-spacing: .5px; }
  .sign--banner .web-band__url { font-size: 44px; }

  .accent-wedge { position: absolute; left: 465px; top: 178px; }

  .council-mark {
    position: absolute;
    display: flex; flex-direction: column; align-items: center; justify-content: center;
    gap: 6px; text-align: center;
    font-family: "Bebas Neue", sans-serif; color: var(--forest-green);
  }
  .council-mark__dot { width: 14px; height: 14px; border-radius: 50%; background: var(--forest-green); }
  .sign--billboard .council-mark { left: 350px; top: 160px; width: 120px; height: 100px; font-size: 18px; line-height: 1.05; }
  .sign--banner .council-mark { left: 578px; top: 40px; width: 200px; height: 165px; font-size: 30px; line-height: 1.05; }

  .scene {
    position: absolute;
    background: linear-gradient(160deg, var(--scene-sky) 0%, var(--scene-leaf) 45%, var(--scene-flame) 100%);
  }
  .sign--billboard .scene { left: 499px; top: 0; width: 321px; height: 273px; clip-path: polygon(30% 0, 100% 0, 100% 100%, 0 100%, 0 40%); }
  .sign--banner .scene { left: 394px; top: 197px; width: 424px; height: 416px; clip-path: polygon(40% 0, 100% 0, 100% 100%, 0 100%, 0 55%); }
</style>
</head>
<body>
  <h2 class="section-label section-label--billboard">Mini-Billboard</h2>

  <section class="sign sign--billboard">
    <h1 class="headline">Protect your home from wildfire<br>Create ignition resistant space</h1>
    <p class="lede">The best way to keep your home from burning is to<br>keep it from catching fire in the first place.</p>
    <div class="web-band">
      <p class="web-band__lead">Learn more at EmberGuard Larkton</p>
      <p class="web-band__url">www.vremwc.org</p>
    </div>
    <div class="council-mark">
      <span class="council-mark__dot"></span>
      <span>ValleyRidge Ember<br>Watch Council</span>
    </div>
    <svg class="accent-wedge" width="48" height="79" viewBox="0 0 48 79" aria-hidden="true">
      <polygon points="0,0 30,0 48,79 48,79" fill="#17473b"/>
      <polygon points="0,0 30,0 48,40 48,79" fill="#17473b"/>
    </svg>
    <div class="scene" role="img" aria-label="Illustration of a two-storey house with a blue roof beside green trees engulfed in wildfire flames"></div>
  </section>

  <section class="sign sign--banner">
    <h1 class="headline">You do not have to live<br>in a forest to be in a<br>wildfire!</h1>
    <p class="call-out">Prepare Now!</p>
    <p class="stakes">Your home...<br>Your loss...<br>Your choice!</p>
    <div class="council-mark">
      <span class="council-mark__dot"></span>
      <span>ValleyRidge Ember<br>Watch Council</span>
    </div>
    <div class="web-band">
      <p class="web-band__lead">Learn more at EmberGuard Larkton</p>
      <p class="web-band__url">www.vremwc.org</p>
    </div>
    <div class="scene" role="img" aria-label="Illustration of a two-storey house with a blue roof beside green trees engulfed in wildfire flames"></div>
  </section>

  <h2 class="section-label section-label--banner">Banner Design</h2>
</body>
</html>
```